Contemporary update for a market leader in foodservice distribution

KORVELT is a market leader in foodservice distribution nationwide.
We have recently adopted a new look and feel for our flagship foodservice rewards programme, and we're looking to have our business cards reflect our new aesthetic. Below is a link to our new rewards website to give you a general idea on the look we're after. https://korveltperks.com.au/

Industry/Entity Type

Distribution

Contact Information for Business Card

Must have space for contact name, position, company name and ABN, address, phone number and direct number, fax, email, and web address.

Font styles to use
Serif
Sans Serif

Requirements
Must have
• We'd like a landscape design, with our 'Tip of the Peak' logo incorporated on either the front or the back of the card. The overall design should be contemporary and professional.
Nice to have
• I have included both the full colour and white version of our company logo - our preference is to have the company logo one solid colour (white, or a shade of grey) although we're also open to designs including the full colour logo. If you are able to incorporate a small Facebook and LinkedIn logo, please do so.
Should not have
• Should not have an over-complicated design. No images of globes, or food.

```html
<!DOCTYPE html>
<html lang="en">
<head>
<meta charset="utf-8">
<title>KORVELT business cards</title>
<link href="https://fonts.googleapis.com/css2?family=Marcellus&family=Open+Sans:wght@400;600;700&display=swap" rel="stylesheet">
<style>
  :root {
    --backdrop: #8a6a48;
    --card-white: #f1f1f1;
    --card-black: #050505;
    --brand-green: #0b8a55;
    --brand-yellow: #f2e10f;
    --ink-dark: #161616;
    --ink-light: #f4f4f4;
    --ink-muted: #d6d6d6;
  }
  * { margin: 0; padding: 0; box-sizing: border-box; }
  html, body { width: 1200px; height: 909px; overflow: hidden; }
  body {
    background: var(--backdrop);
    position: relative;
    font-family: "Open Sans", Arial, sans-serif;
  }
  .card {
    position: absolute;
    width: 580px;
    height: 331px;
    overflow: hidden;
    box-shadow: 0 8px 22px rgba(0,0,0,.35);
  }
  .card-front { left: 80px; top: 90px; background: var(--card-white); }
  .card-back  { left: 540px; top: 480px; background: var(--card-black); }
  .card svg.decor { position: absolute; inset: 0; }

  .wordmark {
    display: flex;
    align-items: center;
    gap: 14px;
  }
  .wordmark .dot {
    width: 34px; height: 34px; border-radius: 50%;
    background: var(--brand-green);
    flex: none;
  }
  .wordmark .name {
    font-family: "Marcellus", Georgia, serif;
    font-size: 60px;
    line-height: 1;
    letter-spacing: 2px;
  }
  .tagline {
    font-weight: 700;
    font-size: 11px;
    letter-spacing: 1.2px;
    text-transform: uppercase;
  }

  .front-brand {
    position: absolute; left: 130px; top: 70px;
    color: var(--ink-dark);
  }
  .front-brand .tagline { margin: 10px 0 0 48px; }
  .front-brand .abn { margin: 14px 0 0 48px; font-size: 17px; }

  .back-content {
    position: absolute; inset: 0;
    display: flex; flex-direction: column; align-items: center;
    color: var(--ink-light);
    padding-top: 34px;
  }
  .back-content .name { color: var(--ink-light); font-size: 56px; }
  .back-content .tagline { margin-top: 8px; font-size: 10.5px; }
  .person-name {
    margin-top: 14px;
    color: var(--brand-yellow);
    font-size: 23px; font-weight: 600;
  }
  .person-role { font-size: 15px; color: var(--ink-muted); }
  .contact { margin-top: 10px; font-size: 14px; text-align: center; line-height: 1.45; }
  .contact svg { width: 11px; height: 11px; vertical-align: -1px; margin-right: 3px; }
  .contact .rule { width: 340px; height: 1px; background: var(--ink-muted); margin: 4px auto; }
  .address { font-size: 15px; }
</style>
</head>
<body>

<section class="card card-front">
  <svg class="decor" width="580" height="331" viewBox="0 0 580 331">
    <line x1="0" y1="298" x2="300" y2="298" stroke="var(--brand-yellow)" stroke-width="9"/>
    <line x1="300" y1="226" x2="580" y2="226" stroke="var(--brand-green)" stroke-width="9"/>
  </svg>
  <div class="front-brand">
    <div class="wordmark"><span class="dot"></span><span class="name">KORVELT</span></div>
    <p class="tagline">Nationwide Catering Supply Network</p>
    <p class="abn">ABN: 41 208 653 917</p>
  </div>
</section>

<section class="card card-back">
  <svg class="decor" width="580" height="331" viewBox="0 0 580 331">
    <path d="M112 0 Q30 165 112 331" fill="none" stroke="var(--brand-yellow)" stroke-width="11"/>
    <path d="M125 0 Q45 165 125 331" fill="none" stroke="var(--brand-green)" stroke-width="9"/>
    <path d="M468 0 Q550 165 468 331" fill="none" stroke="var(--brand-yellow)" stroke-width="11"/>
    <path d="M455 0 Q535 165 455 331" fill="none" stroke="var(--brand-green)" stroke-width="9"/>
  </svg>
  <div class="back-content">
    <div class="wordmark"><span class="dot"></span><span class="name">KORVELT</span></div>
    <p class="tagline">Nationwide Catering Supply Network</p>
    <p class="person-name">Martin Halloway</p>
    <p class="person-role">Managing Director</p>
    <div class="contact">
      <p><svg viewBox="0 0 12 12"><path d="M2 1h3l1 3-2 1a7 7 0 0 0 3 3l1-2 3 1v3a1 1 0 0 1-1 1A10 10 0 0 1 1 2a1 1 0 0 1 1-1z" fill="currentColor"/></svg>555-218-4730</p>
      <p><svg viewBox="0 0 12 12"><rect x="3" y="0.5" width="6" height="11" rx="1" fill="none" stroke="currentColor"/><circle cx="6" cy="9.5" r="0.8" fill="currentColor"/></svg>555-218-4700 / <svg viewBox="0 0 12 12"><rect x="1" y="5" width="10" height="6" fill="currentColor"/><rect x="3" y="1" width="6" height="4" fill="none" stroke="currentColor"/></svg>555-218-4799</p>
      <p><svg viewBox="0 0 12 12"><rect x="1" y="2.5" width="10" height="7" fill="none" stroke="currentColor"/><path d="M1 3l5 4 5-4" fill="none" stroke="currentColor"/></svg>hello@korveltmail.com / <svg viewBox="0 0 12 12"><circle cx="6" cy="6" r="5" fill="none" stroke="currentColor"/><path d="M1 6h10M6 1v10" stroke="currentColor"/></svg>www.korveltaustralian.com</p>
      <div class="rule"></div>
      <p class="address">Penhale Road, Leeds, United Kingdom</p>
    </div>
  </div>
</section>

</body>
</html>
```